Creative Business Card for my Sail Boat.. Tide & Time

Going to order PLASTIC business cards for my boat.. she is a sailing vessel catamaran named Tide & Time..

Target Market(s)

to impress other boaters with a unique designed plastic card

Contact Information for Business Card

S/V Tide & Time
Captain Owen Hartley
hartley@owen.example
Mobile/WhatsApp 1-555-318-7062
www.sailtideandtime.example

Requirements
Must have
• Cool colors. logo.. and info in Business Card Details.. Thanks! Utilize clear or cloudy plastic in design. Thanks

```html
<!DOCTYPE html>
<html lang="en">
<head>
<meta charset="utf-8">
<title>Tide &amp; Time – Business Card</title>
<link rel="stylesheet" href="https://fonts.googleapis.com/css2?family=Arimo:wght@400;700&display=swap">
<style>
  :root {
    --page: #e9e6e1;
    --frost-top: rgba(255,255,255,0.82);
    --frost-bottom: rgba(236,232,226,0.92);
    --edge: rgba(190,182,172,0.9);
    --band: #22a041;
    --band-line: #17803a;
    --accent-line: #9fcfae;
    --name: #d8cbb8;
    --title: #f2f2f2;
    --brand: #8c6f5d;
    --ink: #4a4a4a;
    --icon: #2f8f45;
  }
  * { margin: 0; padding: 0; box-sizing: border-box; }
  html, body {
    width: 1200px; height: 897px; overflow: hidden;
    background: var(--page);
    font-family: "Arimo", Arial, sans-serif;
  }
  .card {
    position: absolute; left: 70px; top: 160px;
    width: 1060px; height: 576px;
    border-radius: 26px;
    border: 2px solid var(--edge);
    background: linear-gradient(160deg, var(--frost-top), var(--frost-bottom));
    box-shadow: 0 10px 30px rgba(0,0,0,0.12);
    overflow: hidden;
  }
  .card__band { position: absolute; inset: 0; width: 100%; height: 100%; }
  .holder { position: absolute; right: 38px; top: 46px; text-align: right; }
  .holder__name { font-weight: 700; font-size: 46px; color: var(--name); letter-spacing: 0.5px; }
  .holder__role { font-size: 34px; color: var(--title); margin-top: 4px; }
  .brand {
    position: absolute; left: 52px; top: 206px;
    display: flex; align-items: center; gap: 14px;
  }
  .brand__name { font-weight: 700; font-size: 60px; color: var(--brand); }
  .brand__dot { width: 44px; height: 44px; border-radius: 50%; background: var(--band); }
  .contacts { position: absolute; left: 46px; top: 378px; list-style: none; }
  .contacts__item {
    display: flex; align-items: center; gap: 16px;
    font-size: 36px; color: var(--ink); height: 56px;
  }
  .contacts__icon { width: 32px; height: 32px; flex: none; }
</style>
</head>
<body>
  <section class="card">
    <svg class="card__band" viewBox="0 0 1060 576" preserveAspectRatio="none" aria-hidden="true">
      <path fill="var(--band)" d="M0 0 H1060 V230 C820 230 620 120 420 90 C240 64 100 90 0 130 Z"/>
      <path fill="none" stroke="var(--band-line)" stroke-width="6" d="M0 160 C110 116 250 100 420 122 C620 150 820 258 1060 258"/>
      <path fill="none" stroke="var(--accent-line)" stroke-width="3" d="M0 182 C120 140 260 126 420 148 C620 176 820 282 1060 282"/>
    </svg>

    <header class="holder">
      <p class="holder__name">Captain Owen Hartley</p>
      <p class="holder__role">CEO / Owner</p>
    </header>

    <div class="brand">
      <span class="brand__name">Tide &amp; Time</span>
      <span class="brand__dot"></span>
    </div>

    <ul class="contacts">
      <li class="contacts__item">
        <svg class="contacts__icon" viewBox="0 0 32 32" aria-hidden="true"><path fill="var(--icon)" d="M4 12 C4 6 28 6 28 12 V15 H22 V12 C18 10 14 10 10 12 V15 H4 Z M8 16 H24 L27 27 H5 Z"/></svg>
        <span>1-555-318-7062</span>
      </li>
      <li class="contacts__item">
        <svg class="contacts__icon" viewBox="0 0 32 32" aria-hidden="true"><rect x="2" y="7" width="28" height="19" fill="var(--icon)"/><path d="M2 7 L16 18 L30 7" fill="none" stroke="#fff" stroke-width="2"/></svg>
        <span>hartley@owen.example</span>
      </li>
      <li class="contacts__item">
        <svg class="contacts__icon" viewBox="0 0 32 32" aria-hidden="true"><circle cx="16" cy="16" r="14" fill="var(--icon)"/><path d="M16 2 V30 M2 16 H30 M16 2 C8 10 8 22 16 30 M16 2 C24 10 24 22 16 30" fill="none" stroke="#fff" stroke-width="1.6"/></svg>
        <span>www.sailtideandtime.example</span>
      </li>
    </ul>
  </section>
</body>
</html>
```